Make a medical leaflet for my patients undergoing ankle blocks

I have a very boring text only leaflet I would like to turn into a professional appealing medical leaflet to give to my patients. I would like to get this onto two pages of a4 if possible and its intended for electronic distribution mainly.
This will be for patients so it must be professional.
It must also contain a copyright logo on it and my name near the start (Dr Tobias Renner) so my colleagues can't use it easily.
Target Market(s)
Patients undergoing surgery
Industry/Entity Type
Medical
Other font styles liked:
- no idea, you tell me
Requirements
Must have
- the information contained on the attachment
- look professional
- a copyright on it
Nice to have
- the fernbrook clinic logo
Should not have
- Any spelling, grammatical or linguistic errors
- Any font less than size 12

```html
<!DOCTYPE html>
<html lang="en">
<head>
<meta charset="utf-8">
<title>Ankle Block – Patient Leaflet</title>
<link href="https://fonts.googleapis.com/css2?family=Montserrat:wght@400;500;600;700;800;900&display=swap" rel="stylesheet">
<style>
:root{
  --blue:#1a8ccc;
  --blue-bright:#0e8fd3;
  --navy:#0b5688;
  --navy-deep:#0a4470;
  --ink:#4a4a4a;
  --ink-dark:#2b2b2b;
  --panel:#f0f1f3;
  --rule:#c9ced4;
  --bg:#7a7a7a;
  --white:#ffffff;
}
*{box-sizing:border-box;margin:0;padding:0}
html,body{width:1200px;height:1200px;overflow:hidden;background:var(--bg);font-family:"Montserrat",sans-serif;color:var(--ink)}
.page{position:absolute;top:234px;width:565px;height:731px;background:var(--white);overflow:hidden}
.page--front{left:20px}
.page--back{left:615px}
.abs{position:absolute}
.name-tag{border:1.5px solid var(--blue);color:var(--blue);font-weight:700;font-size:17px;letter-spacing:.3px;padding:2px 6px;white-space:nowrap;line-height:21px}
.name-tag sup{font-size:8px}
.title{left:39px;top:70px;color:var(--blue);font-weight:900;font-size:50px;line-height:42px;letter-spacing:-1px}
.hero{left:0;top:0;width:565px;height:280px}
p,li{font-size:10px;line-height:12.4px}
.intro{left:23px;top:260px;width:255px}
.intro p{margin-bottom:6px}
.benefits{left:293px;top:230px;width:250px;height:238px;background:var(--panel);padding:10px 10px 0 10px;box-shadow:0 6px 8px -6px rgba(0,0,0,.25)}
.benefits h2{color:var(--blue);font-weight:800;font-size:16px;margin-bottom:6px}
.benefits ol{list-style:none}
.benefits li{position:relative;padding:3px 0 4px 18px;border-bottom:1px solid #dcdfe3;font-size:11px;line-height:13px}
.benefits li:last-child{border-bottom:none}
.benefits li b{color:var(--ink-dark)}
.num{position:absolute;left:0;top:5px;width:11px;height:11px;border-radius:50%;background:var(--blue);color:#fff;font-size:7px;font-weight:700;text-align:center;line-height:11px}
.divider{left:0;top:490px;width:565px;height:1px;background:var(--rule)}
.risks-head{left:0;top:497px;width:565px;text-align:center}
.risks-head h2{color:var(--blue);font-weight:800;font-size:15px;line-height:18px}
.risks-head p{font-weight:600;color:var(--ink-dark);font-size:10px}
.risk{top:539px;width:165px}
.risk + .risk{border-left:1px solid #e2e5e8}
.risk h3{color:var(--blue);font-weight:700;font-size:11.5px;display:inline-block;border-bottom:1.5px solid var(--blue);margin-bottom:4px;line-height:14px}
.risk p,.risk li{font-size:9.6px;line-height:11.6px}
.risk b{color:var(--ink-dark)}
.risk ul{list-style:none}
.risk li::before{content:"• ";color:var(--blue)}
.front-note{left:25px;top:680px;width:515px;text-align:center;font-size:9.6px;line-height:11.6px}
.foot-line{left:0;top:724px;width:565px;height:7px}

.brand{left:18px;top:7px;display:flex;align-items:center;gap:9px}
.brand-square{width:54px;height:46px;background:var(--navy)}
.brand-name{color:var(--navy);font-size:15px;font-weight:500;line-height:18px}
.brand-sub{color:var(--navy);font-size:8px;font-weight:500;margin-top:2px}
.back-rule{left:0;top:60px;width:565px;height:1.5px;background:var(--rule)}
.tab{left:181px;top:54px;width:204px;height:34px}
.tab span{position:absolute;inset:0;color:#fff;font-weight:800;font-size:15px;text-align:center;line-height:32px}
.col h3{color:var(--blue);font-weight:700;font-size:12.5px;line-height:13.5px;margin-bottom:3px}
.col ul{list-style:none}
.col li{position:relative;padding-left:11px;margin-bottom:5px;font-size:10.3px;line-height:12.6px}
.col li::before{content:"•";position:absolute;left:1px;color:var(--blue);font-size:13px;line-height:12px}
.after{left:0;top:322px;width:565px;height:260px}
.after-head{left:0;top:322px;width:565px;height:26px;background:var(--navy);color:#fff;font-weight:800;font-size:17px;text-align:center;line-height:26px}
.after-body{left:22px;top:364px;width:521px;text-align:center;color:#fff}
.after-body p{font-size:10px;line-height:12.2px;margin-bottom:4px}
.alt-title{left:30px;top:588px;color:var(--blue);font-weight:800;font-size:17px}
.alt-col p{margin-bottom:5px;color:var(--ink-dark)}
</style>
</head>
<body>

<section class="page page--front">
  <svg class="abs hero" viewBox="0 0 565 280" aria-hidden="false">
    <defs>
      <linearGradient id="mist" x1="0" y1="0" x2="1" y2="1">
        <stop offset="0" stop-color="#ffffff"/>
        <stop offset="1" stop-color="#e6f1f8"/>
      </linearGradient>
      <linearGradient id="photoTone" x1="0" y1="0" x2="1" y2="1">
        <stop offset="0" stop-color="#d9dde2"/>
        <stop offset=".55" stop-color="#b9c6d2"/>
        <stop offset="1" stop-color="#6e88a3"/>
      </linearGradient>
    </defs>
    <rect width="565" height="280" fill="url(#mist)"/>
    <rect x="230" y="0" width="335" height="245" fill="url(#photoTone)" role="img" aria-label="Photograph of a smiling doctor bandaging the ankle of a young woman seated in a wheelchair"/>
    <path d="M0 195 Q 250 232 565 262 L565 280 L0 280 Z" fill="#ffffff"/>
    <path d="M0 198 Q 150 214 300 240 L 300 246 Q 150 222 0 206 Z" fill="#8fc6e6"/>
    <path d="M150 222 Q 240 238 300 252 L 300 238 Q 230 226 150 214 Z" fill="var(--blue)"/>
  </svg>

  <div class="abs name-tag" style="left:27px;top:32px">DR. TOBIAS RENNER<sup>®</sup></div>
  <h1 class="abs title">ANKLE<br>BLOCK</h1>

  <div class="abs intro">
    <p>You are scheduled to have surgery on your foot. It is my normal practice to offer and perform (with your consent) an ankle block. This is an optional injection of numbing liquid to the nerves which supply your foot. The ankle block can be performed when you are awake, sedated or under general anaesthesia.</p>
    <p>The ankle block can be combined with a general anaesthetic and with sedation. It can also be used to allow surgery to be performed with you wide awake in certain cases.</p>
    <p>Having or not having an ankle block does not change the pre operative fasting guidelines you have been given.</p>
    <p>There is a fee for performing an ankle block. Please consult my initial introductory email and terms of business for details</p>
  </div>

  <div class="abs benefits">
    <h2>WHAT ARE THE BENEFITS</h2>
    <ol>
      <li><span class="num">1</span><b>Excellent pain relief</b> - usually 10 - 14 hours (and rarely 24 - 48 hours)</li>
      <li><span class="num">2</span><b>Avoiding traditional painkillers</b> which resulting in less post operative nausea and vomiting</li>
      <li><span class="num">3</span><b>The option to avoid</b> a general anaesthetic (if you wish)</li>
      <li><span class="num">4</span><b>A faster recovery</b> from the general anaesthetic</li>
      <li><span class="num">5</span><b>Certain surgery requires</b> an overnight stay in hospital without an ankle block</li>
    </ol>
  </div>

  <div class="abs divider"></div>
  <div class="abs risks-head">
    <h2>WHAT ARE THE RISKS?</h2>
    <p>As with all injections, there is the risk of bruising, bleeding and infection.</p>
  </div>

  <div class="abs risk" style="left:31px;padding-right:8px">
    <h3>1 Nerve Damage</h3>
    <p><b>Occurs 1 in 5000 nerve blocks.</b> Creates an area of numbness or weakness/paralysis in some / all the foot. Majority of nerve injuries will heal themselves within a year. <b>There is no treatment to fix it If the block</b> has not worn off after 72 hours please let me know.</p>
  </div>
  <div class="abs risk" style="left:205px;padding-left:9px;padding-right:6px">
    <h3>2 Failure</h3>
    <p><b>The success rate with ankle blocks is 98 - 99%.</b> Some blocks will fail, partially or totally. If total failure, I will discuss repeating the block with your consent.</p>
  </div>
  <div class="abs risk" style="left:372px;padding-left:8px;width:180px">
    <h3>3 Pain during operation</h3>
    <p>If you choose to have wide awake surgery or surgery under sedation. The surgery will stop and <b>I will discuss three options with you</b></p>
    <ul>
      <li><b>More numbing liquid to be injected by the surgeon</b></li>
      <li><b>More sedation / painkiller</b></li>
      <li><b>Having a general</b> anaesthetic</li>
    </ul>
  </div>

  <p class="abs front-note">If you decide to undergo surgery awake or sedated, there is a risk you will need to have a general anaesthetic if you feel pain. This is why the starvation instructions of awake surgery and general anaesthesia are the same.</p>

  <svg class="abs foot-line" viewBox="0 0 565 7" preserveAspectRatio="none" aria-hidden="true">
    <path d="M0 7 Q 280 0 565 2 L565 7 Z" fill="var(--blue)"/>
  </svg>
</section>

<section class="page page--back">
  <div class="abs brand">
    <div class="brand-square"></div>
    <div>
      <div class="brand-name">The Fernbrook Clinic</div>
      <div class="brand-sub">Harbour Gate Hospital · part of Meridian Health UK</div>
    </div>
  </div>
  <div class="abs name-tag" style="left:329px;top:17px">DR. TOBIAS RENNER<sup>®</sup></div>

  <div class="abs back-rule"></div>
  <svg class="abs tab" viewBox="0 0 204 34" aria-hidden="true">
    <path d="M0 0 H204 L190 34 H14 Z" fill="var(--navy)"/>
  </svg>
  <div class="abs tab"><span>HOW IS IT DONE</span></div>

  <div class="abs col" style="left:36px;top:99px;width:232px">
    <h3>IF YOU CHOOSE AWAKE SURGERY OR SURGERY WITH SEDATION</h3>
    <ul>
      <li>The ankle block takes 5 - 10 minutes to perform and requires 4 - 5 injections</li>
      <li>Approximately 10 - 20 minutes to make your foot numb to pain</li>
      <li>I will check the ankle block is working before we start surgery using cold spray</li>
      <li>Sensations of touch, pressure, vibration and movement will still be felt</li>
      <li>I will use a screen so you can't see the surgery (unless you would like to see)</li>
      <li>Some patients bring headphones to block out the noise of the operation.</li>
    </ul>
  </div>
  <div class="abs col" style="left:310px;top:101px;width:225px">
    <h3>IF YOU CHOOSE A GENERAL ANAESTHETIC</h3>
    <ul>
      <li>I will perform the ankle block after I start the general anaesthetic.</li>
      <li>You should wake up from your surgery with a comfortable and numb foot/feet</li>
      <li>If you wake in pain, we can repeat the ankle block or provide traditional painkillers</li>
      <li>Whatever you choose, there will be a cannula placed in your hand and heart and oxygen monitoring throughout.</li>
    </ul>
  </div>

  <svg class="abs after" viewBox="0 0 565 260" aria-hidden="true">
    <path d="M0 0 H565 V238 Q 300 205 0 240 Z" fill="var(--blue-bright)"/>
    <path d="M0 240 Q 300 205 565 238 V246 Q 300 214 0 252 Z" fill="var(--navy-deep)"/>
  </svg>
  <div class="abs after-head">AFTER SURGERY</div>
  <div class="abs after-body">
    <p>You will go to the recovery area and then onto the ward when you are ready. It will be difficult to walk while the block is working so physiotherapists will help you first walk. If you need crutches they will teach you how to use them.</p>
    <p>Your foot will be numb and so you will not feel where your foot is in relation to nearby objects. As a result, it is easy to knock your foot. Please take extra care while your foot is still numb.</p>
    <p>As the block wears off, the foot may feel slightly painful, tingly or hot. At this point you should take your painkillers I have prescribed. Depending on your medical history you will have up to three painkillers. I would suggest to start with all three. You will also have an anti - sickness prescribed if one of the painkillers (typically codeine or morphine) makes you feel sick.</p>
    <p>Occasionally (1 - 2%), pain when the block wears off will be severe. In this case contact your surgeon's secretary. We can use stronger pain medication, but there will be charge in writing and getting the private prescription to you (please see my terms of business) via courier.</p>
  </div>

  <h2 class="abs alt-title">THE ALTERNATIVE</h2>
  <div class="abs alt-col" style="left:32px;top:614px;width:250px">
    <p>If you do not have an ankle block your surgery can still proceed.</p>
    <p>Post operative pain can be managed with traditional painkillers.</p>
    <p>However, you are more likely to need an overnight stay or feel sick after the anaesthetic.</p>
  </div>
  <div class="abs alt-col" style="left:319px;top:611px;width:236px">
    <p>If you have any further questions about an ankle block I will see you the day of your surgery.</p>
    <p>Alternatively, you can request the following optional services (as mentioned in my terms of business).</p>
  </div>

  <svg class="abs foot-line" viewBox="0 0 565 7" preserveAspectRatio="none" aria-hidden="true">
    <path d="M0 2 Q 280 0 565 7 L0 7 Z" fill="var(--blue)"/>
  </svg>
</section>

</body>
</html>
```